Dalton Power Supply, Inc. Business Card Design

We are an Electrical Distributor looking for a Modern, Professional Business Card design.

Target Market(s)

Residential Commercial Industrial

Industry/Entity Type

Electrical

Contact Information for Business Card

Dalton Power Supply, Inc.
418 Maple Ridge Lane
Brookvale, NC 27514
555-214-7630
555-214-8842 Fax
daltonpower@brightmail-example.net

```html
<!DOCTYPE html>
<html lang="en">
<head>
<meta charset="utf-8">
<title>Dalton Power Supply, Inc. – Business Card</title>
<link href="https://fonts.googleapis.com/css2?family=Saira:wght@500;700&display=swap" rel="stylesheet">
<style>
  :root {
    --backdrop: #e9e7e3;
    --card: #ffffff;
    --ink: #111111;
    --brand: #ee5a1e;
    --accent-purple: #6a4aa6;
    --accent-yellow: #ffe400;
    --panel: #000000;
  }
  * { margin: 0; padding: 0; box-sizing: border-box; }
  html, body {
    width: 1000px; height: 1200px; overflow: hidden;
    background: var(--backdrop);
  }
  .sheet { position: relative; width: 1000px; height: 1200px; }
  .card {
    position: absolute; left: 90px; width: 828px; height: 483px;
    background: var(--card); overflow: hidden;
    box-shadow: 0 4px 12px rgba(0,0,0,.25);
    font-family: "Saira", "Arial", sans-serif;
  }
  .card--front { top: 97px; }
  .card--back { top: 631px; }
  .card__panel { position: absolute; left: 0; top: 0; width: 828px; height: 483px; }
  .brand-name {
    position: absolute; left: 46px; top: 56px;
    color: var(--brand); font-weight: 700; line-height: 1;
  }
  .brand-name__main { display: block; font-size: 64px; letter-spacing: 1px; }
  .brand-name__sub { display: block; font-size: 29px; margin-top: 8px; letter-spacing: .3px; }
  .address {
    position: absolute; left: 46px; top: 270px;
    font-size: 21px; font-weight: 500; line-height: 27px; color: var(--ink);
  }
  .contact-list {
    position: absolute; left: 46px; top: 350px; list-style: none;
    font-size: 21px; font-weight: 500; line-height: 27px; color: var(--ink);
  }
  .contact-list li { display: flex; align-items: center; gap: 8px; }
  .contact-list svg { width: 19px; height: 19px; flex: none; }
  .panel-name {
    position: absolute; left: 520px; top: 205px;
    display: flex; align-items: center; gap: 14px;
    color: var(--accent-yellow); font-weight: 700; font-size: 46px; line-height: 1;
    letter-spacing: 1px;
  }
  .panel-name__dot {
    width: 34px; height: 34px; border-radius: 50%; background: var(--accent-yellow);
  }
</style>
</head>
<body>
<div class="sheet">

  <section class="card card--front">
    <svg class="card__panel" viewBox="0 0 828 483" aria-hidden="true">
      <ellipse cx="800" cy="243" rx="398" ry="231" fill="var(--panel)" stroke="var(--accent-yellow)" stroke-width="5"/>
    </svg>
    <h1 class="brand-name">
      <span class="brand-name__main">DALTON</span>
      <span class="brand-name__sub">POWER SUPPLY, INC</span>
    </h1>
    <p class="address">418 Maple Ridge Lane<br>Brookvale, NC 27514</p>
    <ul class="contact-list">
      <li><svg viewBox="0 0 20 20"><rect width="20" height="20" fill="var(--accent-purple)"/><path d="M6 4l3 3-1.5 1.5c.8 1.7 2.2 3.1 4 4L13 11l3 3-2 2C9 16 4 11 4 6z" fill="#fff"/></svg>555-214-7630</li>
      <li><svg viewBox="0 0 20 20"><rect width="20" height="20" fill="var(--accent-purple)"/><rect x="6" y="3" width="8" height="4" fill="#fff"/><rect x="3" y="8" width="14" height="6" fill="#fff"/><rect x="6" y="12" width="8" height="5" fill="#fff" stroke="var(--accent-purple)"/></svg>555-214-8842</li>
      <li><svg viewBox="0 0 20 20"><rect width="20" height="20" fill="var(--accent-purple)"/><rect x="3" y="5" width="14" height="10" fill="#fff"/><path d="M3 5l7 6 7-6" fill="none" stroke="var(--accent-purple)" stroke-width="1.5"/></svg>daltonpower@brightmail-example.net</li>
    </ul>
    <div class="panel-name"><span class="panel-name__dot"></span>DALTON</div>
  </section>

  <section class="card card--back">
    <svg class="card__panel" viewBox="0 0 828 483" aria-hidden="true">
      <ellipse cx="800" cy="243" rx="398" ry="231" fill="var(--panel)" stroke="var(--accent-yellow)" stroke-width="5"/>
    </svg>
    <h1 class="brand-name">
      <span class="brand-name__main">DALTON</span>
      <span class="brand-name__sub">POWER SUPPLY, INC</span>
    </h1>
    <p class="address">418 Maple Ridge Lane<br>Brookvale, NC 27514</p>
    <ul class="contact-list">
      <li><svg viewBox="0 0 20 20"><rect width="20" height="20" fill="var(--accent-purple)"/><path d="M6 4l3 3-1.5 1.5c.8 1.7 2.2 3.1 4 4L13 11l3 3-2 2C9 16 4 11 4 6z" fill="#fff"/></svg>555-214-7630</li>
      <li><svg viewBox="0 0 20 20"><rect width="20" height="20" fill="var(--accent-purple)"/><rect x="6" y="3" width="8" height="4" fill="#fff"/><rect x="3" y="8" width="14" height="6" fill="#fff"/><rect x="6" y="12" width="8" height="5" fill="#fff" stroke="var(--accent-purple)"/></svg>555-214-8842</li>
      <li><svg viewBox="0 0 20 20"><rect width="20" height="20" fill="var(--accent-purple)"/><rect x="3" y="5" width="14" height="10" fill="#fff"/><path d="M3 5l7 6 7-6" fill="none" stroke="var(--accent-purple)" stroke-width="1.5"/></svg>daltonpower@brightmail-example.net</li>
    </ul>
    <div class="panel-name"><span class="panel-name__dot"></span>DALTON</div>
  </section>

</div>
</body>
</html>
```